National Intensive Course Provider needs an advert designed to appear in trams

We need an advertisement designed to put in trams, the dimensions are 660mm wide and 203mm height. We offer intensive driving courses all over the UK, allowing pupils to complete a full driving course within a week/two weeks with both the theory and practical tests included in the course (as required). We would like the colours used to be green and dark blue, maybe red also, whatever looks best from them colours really.

Key Points to highlight:
- Pass your driving test within 1 week
- Start your course as early as next week
- Both tests included as part of your course (if required)

I have attached some images which could be included in the design

```html
<!DOCTYPE html>
<html lang="en">
<head>
<meta charset="utf-8">
<title>Swift Lane – Tram Advert</title>
<link rel="stylesheet" href="https://fonts.googleapis.com/css2?family=Anton&family=Mukta:wght@400&display=swap">
<style>
  :root {
    --navy: #07074a;
    --red: #ee1c24;
    --grey: #8a8a8a;
    --white: #ffffff;
    --silver: #c9cbd0;
    --page: #ececec;
  }
  html, body {
    margin: 0;
    width: 1200px;
    height: 964px;
    overflow: hidden;
    background: var(--page);
  }
  .advert {
    position: absolute;
    left: 40px;
    top: 314px;
    width: 1120px;
    height: 335px;
    background: var(--navy);
    overflow: hidden;
    box-shadow: 0 6px 18px rgba(0,0,0,0.25);
    font-family: "Mukta", sans-serif;
  }
  .advert-shapes {
    position: absolute;
    inset: 0;
    width: 100%;
    height: 100%;
  }
  .headline {
    position: absolute;
    left: 520px;
    top: 18px;
    margin: 0;
    font-family: "Anton", sans-serif;
    font-weight: 400;
    font-size: 64px;
    line-height: 1;
    letter-spacing: 1px;
    color: var(--red);
    text-shadow: 0 0 1px var(--white), 1px 1px 0 var(--white);
  }
  .subhead {
    position: absolute;
    left: 522px;
    top: 96px;
    margin: 0;
    font-size: 29px;
    line-height: 1.2;
    font-weight: 400;
    color: var(--white);
  }
  .subhead .region {
    display: block;
    color: var(--red);
    font-size: 31px;
  }
  .benefits {
    position: absolute;
    left: 522px;
    top: 190px;
    margin: 0;
    padding: 0;
    list-style: none;
    color: var(--white);
    font-size: 20px;
    line-height: 1.3;
  }
  .benefits li {
    position: relative;
    padding-left: 32px;
    margin-bottom: 9px;
  }
  .benefits .wheel {
    position: absolute;
    left: 0;
    top: 5px;
    width: 18px;
    height: 18px;
  }
  .benefits .accent { color: var(--red); }
  .brand {
    position: absolute;
    left: 905px;
    top: 34px;
    display: flex;
    align-items: center;
    gap: 10px;
    font-family: "Mukta", sans-serif;
    font-weight: 400;
    font-size: 34px;
    letter-spacing: 2px;
    color: var(--white);
    line-height: 1;
  }
  .brand .brand-square {
    width: 18px;
    height: 18px;
    background: var(--red);
  }
</style>
</head>
<body>
  <section class="advert">
    <svg class="advert-shapes" viewBox="0 0 1315 393" preserveAspectRatio="none" aria-hidden="false">
      <defs>
        <linearGradient id="lesson-tone" x1="0" y1="0" x2="1" y2="1">
          <stop offset="0" stop-color="#3a3d4a"/>
          <stop offset="0.5" stop-color="#9aa6b8"/>
          <stop offset="1" stop-color="#3b5a8c"/>
        </linearGradient>
        <linearGradient id="pass-tone" x1="0" y1="0" x2="0" y2="1">
          <stop offset="0" stop-color="#5c8a3a"/>
          <stop offset="0.55" stop-color="#8a8f92"/>
          <stop offset="1" stop-color="#c8202a"/>
        </linearGradient>
        <linearGradient id="silver-ring" x1="0" y1="0" x2="1" y2="1">
          <stop offset="0" stop-color="#f4f5f7"/>
          <stop offset="0.5" stop-color="#8e9198"/>
          <stop offset="1" stop-color="#e2e4e8"/>
        </linearGradient>
      </defs>

      <!-- bottom grey band -->
      <polygon points="0,350 195,350 228,393 0,393" fill="var(--grey)"/>
      <!-- red chevron and bottom band -->
      <polygon points="478,0 522,0 568,182 525,393 228,393 195,350 486,350 540,180" fill="var(--red)"/>
      <!-- thin outer chevron line -->
      <polyline points="528,0 578,182 548,393" fill="none" stroke="var(--red)" stroke-width="2"/>
      <!-- driving lesson photo area -->
      <polygon points="0,0 478,0 538,180 484,346 0,346" fill="url(#lesson-tone)" stroke="var(--navy)" stroke-width="3"
               role="img" aria-label="Photo of a smiling learner driver at the wheel with her instructor holding a clipboard"/>

      <!-- successful pupil circle photo -->
      <circle cx="1345" cy="398" r="168" fill="url(#silver-ring)"/>
      <circle cx="1352" cy="398" r="160" fill="url(#pass-tone)"
              role="img" aria-label="Photo of a happy pupil holding his pass certificate beside a red car"/>
    </svg>

    <h1 class="headline">WE OFFER</h1>
    <h2 class="subhead">Intensive Driving Courses<span class="region">All Over The UK</span></h2>

    <ul class="benefits">
      <li>
        <svg class="wheel" viewBox="0 0 20 20" aria-hidden="true"><circle cx="10" cy="10" r="8" fill="none" stroke="var(--red)" stroke-width="2.2"/><circle cx="10" cy="10" r="2" fill="var(--red)"/><path d="M2.5 8.5 H17.5 M10 10 V17.5" stroke="var(--red)" stroke-width="2"/></svg>
        Pass your driving test within <span class="accent">1 week</span>
      </li>
      <li>
        <svg class="wheel" viewBox="0 0 20 20" aria-hidden="true"><circle cx="10" cy="10" r="8" fill="none" stroke="var(--red)" stroke-width="2.2"/><circle cx="10" cy="10" r="2" fill="var(--red)"/><path d="M2.5 8.5 H17.5 M10 10 V17.5" stroke="var(--red)" stroke-width="2"/></svg>
        Start your course as early as <span class="accent">next week</span>
      </li>
      <li>
        <svg class="wheel" viewBox="0 0 20 20" aria-hidden="true"><circle cx="10" cy="10" r="8" fill="none" stroke="var(--red)" stroke-width="2.2"/><circle cx="10" cy="10" r="2" fill="var(--red)"/><path d="M2.5 8.5 H17.5 M10 10 V17.5" stroke="var(--red)" stroke-width="2"/></svg>
        Both tests included as part of your course<br><span class="accent">(if required)</span>
      </li>
    </ul>

    <div class="brand"><span class="brand-square"></span>SWIFT LANE</div>
  </section>
</body>
</html>
```